organic collagen powder needs packaging design

We are about to start a company, that sells nutritional supplements online - especially on Brindlecart. For now we are in need of a packaging design for organic collagen powder (Types I, II and III) maybe including also elastin and eventually hyaluronic acid, which is going to be our first product. We are planning on developing organic nutritional supplements of any kind and this is our initial product. Our upscale products must commincate a solid value proposition, the easygoing solution of a real problem, be understandable by users, perform their task as easily and efficiently as possible, and become better and harder to part with the more they are used. To us it is of the utmost importance to produce and sell organic quality products, which are free of any preservatives, chemical fillers, economic extenders or any other unhealthy ingredients. We want our products to come across as high-quality ones (but in no way conservative or unadventurous), vivid, hip, friendly, reliable, modern and healthy. People - men and women alike - should generally be able to unmistakably connect any of our products immediately to our company and to our product line, so the product packaging should be maximally distinctive. Since we will also need further packaging design for further products in the future please consider that the packaging design is scalable for further products/product-line up. We are thinking about defining our products mainly through design as we are not exactly sure yet, if we want to have a brand name for the products. The products are supposed to address men and women, that are looking for healthy nutrition, that are eager to stay fit and in health and that have a modern view and attitude about life. Although our Collagen will not be vegan (the product itself will be of animal origin = hydrolysed bovine collagen), we basically strive for plant based and vegan nutritional supplements without any unnecessary additives.

Target Market(s)

Hip men and women, who want to stay healthy and fit and have an easygoing, modern attitude to life.

Industry/Entity Type

Nutritional supplements, organic (largely vegan products - when possible and reasonable)

Requirements
Must have
• Maximally distinctive design
Nice to have
• Design should be vivid and happy
Should not have
• simple black packaging with simple writing on it

```html
<!DOCTYPE html>
<html lang="en">
<head>
<meta charset="utf-8">
<title>Collagen Powder Packaging</title>
<link href="https://fonts.googleapis.com/css2?family=Open+Sans:wght@400;700&family=Tinos&display=swap" rel="stylesheet">
<style>
  :root {
    --backdrop: #cbc8c8;
    --mark-grey: #8f8d8d;
    --pouch-black: #0b0b0c;
    --ink-white: #f4f4f4;
    --ink-muted: #8a8a8c;
    --green-deep: #5fb54a;
    --green-light: #b4e39a;
    --orange: #e8742a;
    --sand: #f4c77c;
    --violet: #a467a9;
    --silver-dark: #a9a9ad;
    --silver-light: #f3f3f5;
  }
  * { box-sizing: border-box; margin: 0; padding: 0; }
  html, body { width: 1200px; height: 736px; overflow: hidden; }
  body {
    background: var(--backdrop);
    font-family: "Open Sans", sans-serif;
    position: relative;
  }
  .brand-mark {
    position: absolute; left: 0; top: 92px; width: 1200px;
    text-align: center;
    font-size: 22px; font-weight: 700; letter-spacing: 4px;
    color: var(--mark-grey);
  }
  .pouch {
    position: absolute; top: 237px;
    width: 306px; height: 440px;
    border-radius: 4px 4px 22px 22px;
    overflow: hidden;
    color: var(--ink-white);
  }
  .pouch--type2 { left: 63px; }
  .pouch--type3 { left: 440px; }
  .pouch--type1 { left: 818px; }
  .pouch__face { position: absolute; inset: 0; }
  .pouch__seal-brand {
    position: absolute; left: 103px; top: 88px; width: 100px;
    text-align: center; font-size: 10px; font-weight: 700; letter-spacing: 1.5px;
  }
  .pouch__seal-name {
    position: absolute; left: 103px; top: 140px; width: 100px;
    text-align: center; font-size: 11.5px; font-weight: 700; letter-spacing: 1.2px;
  }
  .pouch__title {
    position: absolute; left: 0; top: 197px; width: 306px;
    text-align: center; font-size: 37px; font-weight: 700; letter-spacing: 4px;
  }
  .pouch__ingredients {
    position: absolute; left: 65px; top: 250px; width: 176px; height: 25px;
    border-radius: 6px;
    font-family: "Tinos", serif; font-size: 9.5px; letter-spacing: 0.6px;
    line-height: 25px; text-align: center; color: #2b2b2b;
  }
  .pouch--type2 .pouch__ingredients { background: var(--green-deep); }
  .pouch--type3 .pouch__ingredients { background: linear-gradient(90deg, var(--orange), var(--sand) 50%, var(--violet)); }
  .pouch--type1 .pouch__ingredients { background: linear-gradient(90deg, var(--silver-dark), var(--silver-light) 50%, var(--silver-dark)); }
  .pouch__category {
    position: absolute; left: 0; top: 383px; width: 306px;
    text-align: center; font-size: 10px; letter-spacing: 2.4px;
  }
  .pouch__net {
    position: absolute; left: 29px; top: 400px; width: 31px; height: 28px;
    border: 1px solid var(--ink-muted); color: var(--ink-muted);
    font-size: 6px; line-height: 1; padding: 2px 0 0 2px;
  }
  .pouch__net strong { display: block; font-size: 10px; font-weight: 400; margin-top: 3px; }
  .pouch__claims {
    position: absolute; left: 62px; top: 403px; width: 182px;
    text-align: center; font-size: 7.5px; line-height: 10px; letter-spacing: 0.6px;
    color: var(--ink-muted);
  }
  .pouch__diet {
    position: absolute; left: 248px; top: 398px; width: 28px; height: 28px;
    border: 1.5px solid var(--ink-muted); border-radius: 4px;
  }
  .pouch__diet-dot {
    position: absolute; left: 7px; top: 7px; width: 11px; height: 11px;
    border: 1.5px solid var(--ink-muted); border-radius: 50%;
  }
  .pouch__diet-label {
    position: absolute; left: 244px; top: 429px; width: 40px;
    font-size: 5px; color: var(--ink-muted); text-align: center;
  }
  .type-badge { position: absolute; left: 123px; top: 300px; width: 60px; height: 60px; }
</style>
</head>
<body>

<div class="brand-mark">VERDALUNE</div>

<!-- Type II -->
<section class="pouch pouch--type2">
  <svg class="pouch__face" viewBox="0 0 306 440" aria-hidden="true">
    <defs>
      <linearGradient id="band-green" x1="0" y1="0" x2="1" y2="0">
        <stop offset="0" style="stop-color:var(--green-deep)"/>
        <stop offset="0.5" style="stop-color:var(--green-light)"/>
        <stop offset="1" style="stop-color:var(--green-deep)"/>
      </linearGradient>
    </defs>
    <rect width="306" height="440" fill="url(#band-green)"/>
    <path d="M0 62 C70 58 88 70 95 110 C102 165 204 165 211 110 C218 70 236 58 306 62 V440 H0Z" fill="var(--pouch-black)"/>
    <circle cx="153" cy="124" r="54" fill="url(#band-green)"/>
    <circle cx="153" cy="120" r="46" fill="var(--pouch-black)"/>
  </svg>
  <div class="pouch__seal-brand">VERDALUNE</div>
  <div class="pouch__seal-name">COLLAGEN</div>
  <h2 class="pouch__title">COLLAGEN</h2>
  <p class="pouch__ingredients">ELASTIN + HYALURONIC ACID</p>
  <svg class="type-badge" viewBox="0 0 60 60" aria-label="Type 2">
    <defs><path id="arc2" d="M10 44 A24 24 0 0 1 30 6"/></defs>
    <circle cx="30" cy="30" r="24" fill="none" stroke="var(--green-deep)" stroke-width="8"/>
    <circle cx="30" cy="30" r="16" fill="none" stroke="var(--green-light)" stroke-width="1"/>
    <text font-family="Open Sans, sans-serif" font-size="8" font-weight="700" fill="#111"><textPath href="#arc2">TYPE</textPath></text>
    <text x="32" y="42" text-anchor="middle" font-family="Tinos, serif" font-size="34" fill="var(--ink-white)">2</text>
  </svg>
  <p class="pouch__category">NUTRITIONAL SUPPLEMENTS</p>
  <div class="pouch__net">NET WT<strong>250g</strong></div>
  <p class="pouch__claims">No Dairy Ingredients | Non-GMO<br>No Soy Ingredients | Paleo Friendly</p>
  <div class="pouch__diet"><span class="pouch__diet-dot"></span></div>
  <span class="pouch__diet-label">NON-VEG</span>
</section>

<!-- Type III -->
<section class="pouch pouch--type3">
  <svg class="pouch__face" viewBox="0 0 306 440" aria-hidden="true">
    <defs>
      <linearGradient id="band-sunset" x1="0" y1="0" x2="1" y2="0">
        <stop offset="0" style="stop-color:var(--orange)"/>
        <stop offset="0.45" style="stop-color:var(--sand)"/>
        <stop offset="1" style="stop-color:var(--violet)"/>
      </linearGradient>
    </defs>
    <rect width="306" height="440" fill="url(#band-sunset)"/>
    <path d="M0 62 C70 58 88 70 95 110 C102 165 204 165 211 110 C218 70 236 58 306 62 V440 H0Z" fill="var(--pouch-black)"/>
    <circle cx="153" cy="124" r="54" fill="url(#band-sunset)"/>
    <circle cx="153" cy="120" r="46" fill="var(--pouch-black)"/>
  </svg>
  <div class="pouch__seal-brand">VERDALUNE</div>
  <div class="pouch__seal-name">COLLAGEN</div>
  <h2 class="pouch__title">COLLAGEN</h2>
  <p class="pouch__ingredients">ELASTIN + HYALURONIC ACID</p>
  <svg class="type-badge" viewBox="0 0 60 60" aria-label="Type 3">
    <defs>
      <path id="arc3" d="M10 44 A24 24 0 0 1 30 6"/>
      <linearGradient id="ring-sunset" x1="0" y1="0" x2="1" y2="0">
        <stop offset="0" style="stop-color:var(--orange)"/>
        <stop offset="1" style="stop-color:var(--violet)"/>
      </linearGradient>
    </defs>
    <circle cx="30" cy="30" r="24" fill="none" stroke="url(#ring-sunset)" stroke-width="8"/>
    <circle cx="30" cy="30" r="16" fill="none" stroke="var(--sand)" stroke-width="1"/>
    <text font-family="Open Sans, sans-serif" font-size="8" font-weight="700" fill="#111"><textPath href="#arc3">TYPE</textPath></text>
    <text x="32" y="42" text-anchor="middle" font-family="Tinos, serif" font-size="34" fill="var(--ink-white)">3</text>
  </svg>
  <p class="pouch__category">NUTRITIONAL SUPPLEMENTS</p>
  <div class="pouch__net">NET WT<strong>250g</strong></div>
  <p class="pouch__claims">No Dairy Ingredients | Non-GMO<br>No Soy Ingredients | Paleo Friendly</p>
  <div class="pouch__diet"><span class="pouch__diet-dot"></span></div>
  <span class="pouch__diet-label">NON-VEG</span>
</section>

<!-- Type I -->
<section class="pouch pouch--type1">
  <svg class="pouch__face" viewBox="0 0 306 440" aria-hidden="true">
    <defs>
      <linearGradient id="band-silver" x1="0" y1="0" x2="1" y2="0">
        <stop offset="0" style="stop-color:var(--silver-dark)"/>
        <stop offset="0.5" style="stop-color:var(--silver-light)"/>
        <stop offset="1" style="stop-color:var(--silver-dark)"/>
      </linearGradient>
    </defs>
    <rect width="306" height="440" fill="url(#band-silver)"/>
    <path d="M0 62 C70 58 88 70 95 110 C102 165 204 165 211 110 C218 70 236 58 306 62 V440 H0Z" fill="var(--pouch-black)"/>
    <circle cx="153" cy="124" r="54" fill="url(#band-silver)"/>
    <circle cx="153" cy="120" r="46" fill="var(--pouch-black)"/>
  </svg>
  <div class="pouch__seal-brand">VERDALUNE</div>
  <div class="pouch__seal-name">COLLAGEN</div>
  <h2 class="pouch__title">COLLAGEN</h2>
  <p class="pouch__ingredients">ELASTIN + HYALURONIC ACID</p>
  <svg class="type-badge" viewBox="0 0 60 60" aria-label="Type 1">
    <defs><path id="arc1" d="M10 44 A24 24 0 0 1 30 6"/></defs>
    <circle cx="30" cy="30" r="24" fill="none" stroke="var(--silver-dark)" stroke-width="8"/>
    <circle cx="30" cy="30" r="16" fill="none" stroke="var(--silver-light)" stroke-width="1"/>
    <text font-family="Open Sans, sans-serif" font-size="8" font-weight="700" fill="#111"><textPath href="#arc1">TYPE</textPath></text>
    <text x="32" y="42" text-anchor="middle" font-family="Tinos, serif" font-size="34" fill="var(--ink-white)">1</text>
  </svg>
  <p class="pouch__category">NUTRITIONAL SUPPLEMENTS</p>
  <div class="pouch__net">NET WT<strong>250g</strong></div>
  <p class="pouch__claims">No Dairy Ingredients | Non-GMO<br>No Soy Ingredients | Paleo Friendly</p>
  <div class="pouch__diet"><span class="pouch__diet-dot"></span></div>
  <span class="pouch__diet-label">NON-VEG</span>
</section>

</body>
</html>
```